BUSINESS CARD FOR GUITAR SCHOOL

I would like to design a business card for my Guitar Music School. The school is called "Pluck & Meadow".

The card should be yellow.

Target Market(s)

18-35 years old

Industry/Entity Type

School

Contact Information for Business Card

I would like to design a business card for my Guitar Music School. The school is called "Pluck & Meadow". The card should be yellow.

Card must be consistent with my website design: www.pluckandmeadow.com.sg

Requirements
Must have
• 1) Name of Company
• 2) Company Logo
• 3) Name of Employee
• 4) Position of Employee
• 5) Contact Number
• 6) Address
Nice to have
• Creative Design
• Card must be consistent with my website design: www.pluckandmeadow.com.sg
Should not have
• Boring Design

```html
<!DOCTYPE html>
<html lang="en">
<head>
<meta charset="utf-8">
<title>Pluck &amp; Meadow — Business Card</title>
<link href="https://fonts.googleapis.com/css2?family=Lato:wght@400;700;900&display=swap" rel="stylesheet">
<style>
  :root {
    --backdrop: #2a2a2a;
    --card-dark: #2b2b2b;
    --card-yellow: #f7b928;
    --accent-yellow: #f5b820;
    --ink: #1f1f1f;
    --muted: #d9d9d9;
  }
  * { box-sizing: border-box; margin: 0; padding: 0; }
  html, body {
    width: 1200px; height: 873px; overflow: hidden;
    background: var(--backdrop);
    font-family: "Lato", Arial, sans-serif;
  }
  .stage {
    position: relative; width: 1200px; height: 873px;
    display: flex; align-items: center; justify-content: center; gap: 40px;
  }
  .card {
    position: relative; width: 540px; height: 310px;
    border-radius: 16px; overflow: hidden;
  }
  /* Front */
  .card--front { background: var(--card-dark); color: var(--accent-yellow); }
  .front__brand {
    position: absolute; left: 70px; top: 96px;
    font-weight: 900; font-size: 52px; line-height: 1; letter-spacing: -1px;
  }
  .front__tagline {
    position: absolute; left: 196px; top: 160px;
    font-size: 15px; font-weight: 400;
  }
  .front__web {
    position: absolute; left: 0; right: 0; bottom: 44px; text-align: center;
    font-size: 12px; letter-spacing: 3px;
  }
  /* Back */
  .card--back { background: var(--card-yellow); color: var(--ink); }
  .back__brand {
    position: absolute; left: 32px; top: 78px;
    font-weight: 900; font-size: 30px; line-height: 1; letter-spacing: -0.5px;
  }
  .back__tagline {
    position: absolute; left: 92px; top: 112px; font-size: 10px;
  }
  .back__person { position: absolute; right: 34px; top: 34px; text-align: right; }
  .person__name { font-weight: 900; font-size: 20px; }
  .person__role { font-size: 12px; color: #ffffff; margin-top: 2px; }
  .rule { position: absolute; height: 2px; background: var(--ink); }
  .rule--upper { left: 250px; right: 34px; top: 108px; }
  .rule--lower { left: 32px; width: 220px; top: 196px; }
  .back__offer { position: absolute; right: 34px; top: 150px; text-align: right; }
  .offer__lead { font-weight: 900; font-size: 19px; color: var(--muted); }
  .offer__detail { font-size: 14px; font-weight: 400; }
  .contacts { position: absolute; left: 32px; top: 208px; list-style: none; }
  .contacts li {
    display: flex; align-items: flex-start; gap: 12px;
    font-size: 14px; font-weight: 700; line-height: 1.25; margin-bottom: 5px;
  }
  .contacts svg { width: 15px; height: 15px; flex: none; margin-top: 1px; fill: #ffffff; }
</style>
</head>
<body>
<main class="stage">
  <section class="card card--front" aria-label="Card front">
    <div class="front__brand">Pluck &amp; Meadow</div>
    <div class="front__tagline">Taking Worship to the Next Level</div>
    <div class="front__web">www.pluckandmeadow.com.sg</div>
  </section>

  <section class="card card--back" aria-label="Card back">
    <div class="back__person">
      <div class="person__name">Dana Whitfield</div>
      <div class="person__role">Owner / Founder</div>
    </div>
    <div class="back__brand">Pluck &amp; Meadow</div>
    <div class="back__tagline">Taking Worship to the Next Level</div>
    <div class="rule rule--upper"></div>
    <div class="back__offer">
      <div class="offer__lead">JOIN OUR</div>
      <div class="offer__detail">FREE TRIAL CLASS</div>
    </div>
    <div class="rule rule--lower"></div>
    <ul class="contacts">
      <li>
        <svg viewBox="0 0 16 16" aria-hidden="true"><path d="M1 5c0-2 3-3 7-3s7 1 7 3v1h-4V5H5v1H1zM3 8h10l1 6H2z"/></svg>
        +65 9150 4482
      </li>
      <li>
        <svg viewBox="0 0 16 16" aria-hidden="true"><path d="M1 3h14v10H1zM2 4l6 5 6-5v1L8 10 2 5z" fill-rule="evenodd"/></svg>
        hello@pluckandmeadow.com.sg
      </li>
      <li>
        <svg viewBox="0 0 16 16" aria-hidden="true"><path d="M8 1a5 5 0 0 1 5 5c0 4-5 9-5 9S3 10 3 6a5 5 0 0 1 5-5zm0 3a2 2 0 1 0 0 4 2 2 0 0 0 0-4z" fill-rule="evenodd"/></svg>
        <span>27 Kestrel Lane, Harbour Court,<br>B #04-12, Singapore</span>
      </li>
    </ul>
  </section>
</main>
</body>
</html>
```